Webdesign für KFZ-Service-Betrieb
Zielgruppe
Wartung, Reparatur und Instandsetzung von Kraftfahrzeugen aller Marken.
Reifenhandel, Old- und Youngtimer-Service, An- und Verkauf von Fahrzeugen.
Aufgabenstellung
Firmenfarbe ist blau.
Moderner, Übersichtlicher und Transparenter Auftritt erwünscht.

```html
<!DOCTYPE html>
<html lang="de">
<head>
<meta charset="utf-8">
<title>KFZ-Service – Wir über uns</title>
<link rel="stylesheet" href="https://fonts.googleapis.com/css2?family=Libre+Baskerville:wght@400;700&family=Lustria&family=Open+Sans:wght@600&family=Montserrat:wght@500&display=swap">
<style>
  :root {
    --brand-blue: #23309a;
    --text-blue: #2b3194;
    --white: #ffffff;
    --hero-top: #8c93a8;
    --hero-mid: #3a4470;
    --hero-low: #1f2540;
  }
  * { margin: 0; padding: 0; box-sizing: border-box; }
  html, body { width: 1200px; height: 2396px; overflow: hidden; background: var(--white); }
  .page { position: relative; width: 1200px; height: 2396px; color: var(--text-blue); font-family: "Lustria", Georgia, serif; }
  .abs { position: absolute; }

  .logo { left: 56px; top: 30px; font-family: "Montserrat", Arial, sans-serif; font-weight: 500; font-size: 22px; line-height: 28px; letter-spacing: 4px; color: var(--brand-blue); }
  .nav-link { left: 0; width: 1216px; top: 84px; text-align: center; font-family: "Montserrat", Arial, sans-serif; font-weight: 500; font-size: 27px; letter-spacing: 5px; color: var(--brand-blue); }

  .hero { left: 0; top: 149px; width: 1200px; height: 478px; background: linear-gradient(180deg, var(--hero-top) 0%, var(--hero-mid) 55%, var(--hero-low) 100%); }
  .hero-title { position: absolute; left: 0; right: 0; top: 185px; text-align: center; font-family: "Open Sans", Arial, sans-serif; font-weight: 600; font-size: 31px; line-height: 59px; letter-spacing: 6.5px; color: var(--white); }

  .intro-title { left: 0; width: 1216px; top: 686px; text-align: center; font-family: "Libre Baskerville", Georgia, serif; font-weight: 700; font-size: 37px; color: var(--brand-blue); }
  .intro-text { left: 20px; width: 1160px; top: 738px; text-align: center; font-size: 18px; line-height: 23.5px; }

  .accent-bar { height: 10px; background: var(--brand-blue); }
  .service-title { font-family: "Libre Baskerville", Georgia, serif; font-weight: 700; font-size: 25px; line-height: 35px; letter-spacing: 0.5px; color: var(--brand-blue); }
  .service-text { font-size: 18.5px; line-height: 35px; white-space: nowrap; }
  .read-more { font-size: 26px; color: var(--text-blue); }

  .footer { left: 0; top: 2315px; width: 1200px; height: 81px; background: var(--brand-blue); color: var(--white); }
  .footer-contact { position: absolute; left: 68px; top: 14px; font-family: "Libre Baskerville", Georgia, serif; font-weight: 700; font-size: 16px; line-height: 25px; letter-spacing: 3px; text-align: center; }
  .footer-hours { position: absolute; left: 300px; width: 420px; top: 9px; text-align: center; font-family: "Libre Baskerville", Georgia, serif; font-size: 15px; line-height: 28px; }
  .footer-phone-icon { position: absolute; left: 880px; top: 18px; }
  .footer-phones { position: absolute; left: 934px; top: 6px; font-family: "Libre Baskerville", Georgia, serif; font-weight: 700; font-size: 17px; line-height: 28px; letter-spacing: 1px; }
</style>
</head>
<body>
<div class="page">
  <header>
    <div class="abs logo">YOUR<br>LOGO<br>HERE</div>
    <nav class="abs nav-link">Wir über uns</nav>
  </header>

  <section class="abs hero" role="img" aria-label="Zwei Mechaniker in blauen Overalls an einem Auto mit geöffneter Motorhaube in der Werkstatt">
    <h1 class="hero-title">Wartung, Reparatur und Instandsetzung<br>von Kraftfahrzeugen aller Marken.</h1>
  </section>

  <section>
    <h2 class="abs intro-title">PRO SOLUTIONS</h2>
    <p class="abs intro-text">loremp loremp loremp lorem lormel loremp lorem lorem lorem lorem lorem loremp loremp loremp loore lorem<br>lorem&nbsp; lorem lorem lorem&nbsp; loremp loremp loremp loremp loremp lorem lorem loremp loremp loremp lorem lormel loremp<br>lorem lorem lorem lorem&nbsp; lorem loremp loremp loremp loore lorem lorem&nbsp; lorem lorem lorem&nbsp; loremp loremp<br>loremp loremp loremp lorem lorem</p>
  </section>

  <article>
    <div class="abs accent-bar" style="left:52px; top:903px; width:498px;"></div>
    <h3 class="abs service-title" style="left:54px; top:936px;">WARTUNG, REPARATUR UND<br>INSTANDSETZUNG</h3>
    <p class="abs service-text" style="left:54px; top:1008px;">loremp loremp loremp lorem lormel loremp lorem lorem<br>lorem loremlorem loremp loremp loremp loore lorem<br>lorem&nbsp; lorem lorem lorem loremp loremp loremp loremp<br>loremp lorem lorem</p>
    <a class="abs read-more" style="left:399px; top:1214px;">Read more</a>
    <div class="abs" style="left:635px; top:903px; width:509px; height:419px; background:linear-gradient(135deg,#e7b818 0%,#c99a1a 35%,#2c3470 60%,#d9dade 100%);" role="img" aria-label="Mechaniker in blauem Shirt arbeitet am Motor eines weißen Autos"></div>
  </article>

  <article>
    <div class="abs" style="left:52px; top:1375px; width:496px; height:418px; background:linear-gradient(160deg,#6b6b6b 0%,#2b2b2b 55%,#1a1a1a 100%);" role="img" aria-label="Vier Autoreifen auf einer Straße"></div>
    <div class="abs accent-bar" style="left:635px; top:1375px; width:509px;"></div>
    <h3 class="abs service-title" style="left:634px; top:1415px;">REIFENHANDEL</h3>
    <p class="abs service-text" style="left:634px; top:1452px;">loremp loremp loremp lorem lormel loremp lorem lorem<br>lorem lorem lorem loremp loremp loremp loore lorem<br>lorem&nbsp; lorem lorem lorem loremp loremp loremp loremp<br>loremp lorem lorem</p>
    <a class="abs read-more" style="left:994px; top:1644px;">Read more</a>
  </article>

  <article>
    <div class="abs accent-bar" style="left:41px; top:1846px; width:512px;"></div>
    <h3 class="abs service-title" style="left:59px; top:1887px;">AN- UND VERKAUF<br>VON FAHRZEUGEN</h3>
    <p class="abs service-text" style="left:59px; top:1959px;">loremp loremp loremp lorem lormel loremp lorem lorem<br>lorem lorem lorem loremp loremp loremp loore lorem<br>lorem&nbsp; lorem lorem lorem loremp loremp loremp loremp<br>loremp lorem lorem</p>
    <a class="abs read-more" style="left:397px; top:2116px;">Read more</a>
    <div class="abs" style="left:637px; top:1846px; width:505px; height:407px; background:linear-gradient(180deg,#3a3a3a 0%,#8a8a8a 50%,#cfcfcf 100%);" role="img" aria-label="Schwarz-weiß Foto eines klassischen Cabrios mit Fahrern"></div>
  </article>

  <footer class="abs footer">
    <div class="footer-contact">OUR<br>CONTACT</div>
    <div class="footer-hours">Öffnungszeiten: Mo.-Fr.: 08.00 Uhr - 18.30 Uhr<br>Sa.: 09.00 Uhr-13.00 Uhr</div>
    <svg class="footer-phone-icon" width="46" height="46" viewBox="0 0 24 24" aria-hidden="true">
      <path fill="#ffffff" d="M6.6 10.8c1.4 2.8 3.8 5.1 6.6 6.6l2.2-2.2c.3-.3.7-.4 1-.2 1.1.4 2.3.6 3.6.6.6 0 1 .4 1 1V20c0 .6-.4 1-1 1C10.6 21 3 13.4 3 4c0-.6.4-1 1-1h3.5c.6 0 1 .4 1 1 0 1.3.2 2.5.6 3.6.1.3 0 .7-.2 1L6.6 10.8z"/>
    </svg>
    <div class="footer-phones">800-5550-1427<br>800-5550-1428</div>
  </footer>
</div>
</body>
</html>
```